Easter Invitation for Harbor Grace Church

I would like a 6x9 postcard mailer inviting people to our Easter services at Harbor Grace Church in Milwaukee Wisconsin. The template is included
I would like it to be a simple invitation.
Options for wording on one side
-Easter
-Easter at Harbor Grace
-Harbor Grace This Easter
-You're Invited
We could also consider putting the date and time on this side also (Saturday, March 30th @5pm)
Side 2 would have our Logo (We do have the AI or EPS file if needed), Date, Name, Address, QR Code, phone, Website Information.
Saturday, March 30th at 5pm
Harbor Grace Church
1184 W. 37th Street
Milwaukee, WI 53208
Ph: 414-555-0172
Website: www.harborgracefold.org
tagline: A Home Where Welcomed Hearts Welcome Hearts

```html
<!DOCTYPE html>
<html lang="en">
<head>
<meta charset="utf-8">
<title>Harbor Grace Church – Easter Postcard</title>
<link rel="stylesheet" href="https://fonts.googleapis.com/css2?family=Crimson+Pro:wght@400;500&family=Montserrat:wght@400;500;600&display=swap">
<style>
  :root {
    --backdrop: #a9a9a9;
    --paper: #f4f1ea;
    --ink: #2a2a2a;
    --navy: #1f2a6b;
    --gold: #f0c77a;
    --cream: #fbe6bd;
    --maroon-deep: #3a0d22;
    --maroon: #6e1a2c;
    --ember: #d2521e;
    --glow: #ffb347;
    --light: #fff2c4;
  }
  * { box-sizing: border-box; margin: 0; padding: 0; }
  html, body { width: 1200px; height: 1200px; overflow: hidden; }
  body {
    background: var(--backdrop);
    position: relative;
    font-family: "Montserrat", sans-serif;
  }
  .postcard {
    position: absolute;
    left: 210px;
    width: 780px;
    height: 520px;
    overflow: hidden;
    box-shadow: 0 6px 18px rgba(0,0,0,0.18);
  }
  .postcard--front { top: 53px; }
  .postcard--back { top: 627px; background: var(--paper); }

  .front-artwork {
    position: absolute;
    inset: 0;
    background:
      radial-gradient(ellipse 20% 26% at 67% 22%, var(--light) 0%, var(--light) 55%, rgba(255,242,196,0) 100%),
      radial-gradient(ellipse 42% 70% at 66% 45%, var(--glow) 0%, var(--ember) 45%, rgba(110,26,44,0) 85%),
      linear-gradient(100deg, var(--maroon-deep) 0%, var(--maroon) 35%, #9c2e22 60%, var(--maroon) 85%, var(--maroon-deep) 100%);
  }
  .front-headline {
    position: absolute;
    left: 100px;
    top: 48px;
    font-family: "Crimson Pro", serif;
    font-weight: 400;
    font-size: 56px;
    line-height: 1.0;
    color: var(--gold);
  }
  .front-name {
    position: absolute;
    right: 30px;
    bottom: 28px;
    display: flex;
    align-items: center;
    gap: 8px;
    font-family: "Crimson Pro", serif;
    font-weight: 500;
    font-size: 26px;
    color: var(--cream);
  }
  .front-name .mark {
    width: 14px;
    height: 14px;
    background: var(--cream);
  }

  .back-content {
    position: absolute;
    left: 44px;
    top: 40px;
    color: var(--ink);
  }
  .back-name {
    display: flex;
    align-items: center;
    gap: 8px;
    font-weight: 600;
    font-size: 26px;
    color: var(--navy);
    margin-bottom: 14px;
  }
  .back-name .mark {
    width: 14px;
    height: 14px;
    background: var(--navy);
  }
  .event-details {
    font-style: normal;
    font-size: 14px;
    line-height: 1.25;
    letter-spacing: 0.3px;
  }
  .tagline {
    margin-top: 12px;
    font-size: 14px;
    letter-spacing: 0.3px;
  }
  .stamp-box {
    position: absolute;
    right: 44px;
    top: 40px;
    width: 110px;
    height: 110px;
    border: 1px solid var(--ink);
    display: flex;
    align-items: center;
    justify-content: center;
    text-align: center;
    font-size: 11px;
    line-height: 1.15;
    letter-spacing: 1.5px;
    color: var(--ink);
  }
</style>
</head>
<body>
  <section class="postcard postcard--front">
    <div class="front-artwork" role="img" aria-label="Illustration of a robed figure walking out of a glowing rock tomb toward a bright opening with three crosses on a distant hill"></div>
    <h1 class="front-headline">Harbor Grace<br>This<br>Easter</h1>
    <div class="front-name"><span class="mark"></span>Harbor Grace</div>
  </section>

  <section class="postcard postcard--back">
    <div class="back-content">
      <div class="back-name"><span class="mark"></span>Harbor Grace</div>
      <address class="event-details">
        Saturday, March 30th at 5pm<br>
        Harbor Grace Church<br>
        1184 W. 37th Street<br>
        Milwaukee, WI 53208<br>
        Ph: 414-555-0172<br>
        Website: www.harborgracefold.org
      </address>
      <p class="tagline">A Home Where Welcomed Hearts Welcome Hearts</p>
    </div>
    <div class="stamp-box">LEAVE<br>EMPTY<br>FOR<br>STAMP</div>
  </section>
</body>
</html>
```